Business Card Design Project

We are rebranding an existing automotive collision repair business. The business is called harrowell works. I have attached logo but I'm not tied to that. I want to leave this wide open.

I want this card to say we are professional, competent, cutting edge. We are focused on customers and use a lot of the latest technology to make the customer experience different. We sign customers in on Vextabs. Paperwork I signed electronically and updates are sent via text, email, logging on a website or as they wish. I want this innovation and image to come through in our cards

Target Market(s)

60%. Women 40% men. Age 35-60

Industry/Entity Type

Automotive

Requirements
Must have
• The card must have name, title, phone,email, cell, web page

```html
<!DOCTYPE html>
<html lang="en">
<head>
<meta charset="utf-8">
<title>harrowell works business card</title>
<link rel="stylesheet" href="https://fonts.googleapis.com/css2?family=Roboto:wght@300;400&display=swap">
<style>
  :root {
    --page: #ffffff;
    --card-front: #dcdddf;
    --brand-green: #4ab847;
    --wordmark: #58a944;
    --ink-light: #ffffff;
    --title-muted: #b9e3b4;
    --shadow: rgba(0, 0, 0, 0.22);
  }
  * { box-sizing: border-box; margin: 0; padding: 0; }
  html, body {
    width: 1200px;
    height: 800px;
    overflow: hidden;
    background: var(--page);
    font-family: "Roboto", "Helvetica Neue", Arial, sans-serif;
    font-weight: 300;
  }
  .canvas {
    position: relative;
    width: 1200px;
    height: 800px;
  }
  .card {
    position: absolute;
    left: 320px;
    width: 560px;
    height: 320px;
    box-shadow: 0 14px 18px -10px var(--shadow);
  }
  .card--front {
    top: 60px;
    background: var(--card-front);
    display: flex;
    align-items: center;
    justify-content: center;
  }
  .wordmark {
    color: var(--wordmark);
    font-weight: 400;
    font-size: 40px;
    letter-spacing: 0.5px;
  }
  .card--back {
    top: 420px;
    background: var(--brand-green);
    color: var(--ink-light);
  }
  .holder {
    position: absolute;
    top: 20px;
    right: 20px;
    display: flex;
    align-items: baseline;
    gap: 8px;
  }
  .holder__name { font-size: 27px; }
  .holder__title { font-size: 13px; color: var(--title-muted); }
  .contacts {
    position: absolute;
    left: 24px;
    top: 180px;
    list-style: none;
  }
  .contacts__item {
    display: flex;
    align-items: center;
    height: 29px;
    font-size: 17px;
  }
  .contacts__icon {
    width: 18px;
    height: 18px;
    margin-right: 14px;
    fill: none;
    stroke: var(--ink-light);
    stroke-width: 1.1;
  }
</style>
</head>
<body>
<main class="canvas">
  <section class="card card--front" aria-label="Card front">
    <span class="wordmark">harrowell works</span>
  </section>

  <section class="card card--back" aria-label="Card back">
    <div class="holder">
      <span class="holder__name">Owen Marsh</span>
      <span class="holder__title">Director</span>
    </div>
    <ul class="contacts">
      <li class="contacts__item">
        <svg class="contacts__icon" viewBox="0 0 18 18"><rect x="2" y="4" width="14" height="10"/><path d="M2 4l7 6 7-6"/></svg>
        abcde@harrowellworks.com
      </li>
      <li class="contacts__item">
        <svg class="contacts__icon" viewBox="0 0 18 18"><circle cx="9" cy="9" r="7"/><ellipse cx="9" cy="9" rx="3" ry="7"/><path d="M2 9h14M3.5 5h11M3.5 13h11"/></svg>
        www.harrowellworks.com
      </li>
      <li class="contacts__item">
        <svg class="contacts__icon" viewBox="0 0 18 18"><path d="M4 2.5l3 3-1.6 2a9 9 0 0 0 5.1 5.1l2-1.6 3 3-2 2C8 15.5 2.5 10 2 4.5z"/></svg>
        +1 (800) 555-0142
      </li>
      <li class="contacts__item">
        <svg class="contacts__icon" viewBox="0 0 18 18"><rect x="5" y="1.5" width="8" height="15" rx="1"/><path d="M8 14h2"/></svg>
        +1 (800) 555-0142
      </li>
    </ul>
  </section>
</main>
</body>
</html>
```